Web Design for an Online Dating Web Site

We need an uncoded web design for a new online dating web site called zMatchy.net. Simplicity and boldness are the key factors in the successful design.
Please look at the requirements document attached for details.
Updates
Dear all,
Please AVOID USING A PICTURE OF A HAPPY COUPLE ON THE HOME PAGE of the site. We highly want to move away from this space as it makes our web site just like another dating web site.
We like something simple with web 2.0 look and feel. The examples in the Requirements Document are exactly the design we are after.
Regards
Tarn
Industry/Entity Type
Dating
Look and feel
Each slider illustrates characteristics of the customer's brand and the style your logo design should communicate.

```html
<!DOCTYPE html>
<html lang="en">
<head>
<meta charset="utf-8">
<title>zMatchy.net – Connections that just click</title>
<link href="https://fonts.googleapis.com/css2?family=Sniglet&family=Questrial&family=Arimo:wght@400;700&display=swap" rel="stylesheet">
<style>
:root{
  --pink:#e8177f;
  --pink-dark:#b80f62;
  --ink:#4a4a4a;
  --ink-soft:#666;
  --ink-faint:#8a8a8a;
  --page:#cdcdcd;
  --panel:#d6d6d6;
  --field:#bdbdbd;
  --field-line:#a9a9a9;
  --footer:#8f8f8f;
  --white:#fff;
}
*{box-sizing:border-box;margin:0;padding:0}
html,body{width:840px;height:1200px;overflow:hidden}
body{position:relative;background:linear-gradient(#dedede 0,#cfcfcf 380px,#c6c6c6 790px);font-family:'Questrial',sans-serif;color:var(--ink)}
.abs{position:absolute}
.display{font-family:'Sniglet',sans-serif}

/* header */
.site-header{left:0;top:0;width:840px;height:91px;background:radial-gradient(ellipse at 50% 30%,#f2f2f2,#d8d8d8 70%)}
.brand{left:0;width:840px;top:22px;text-align:center;font-family:'Sniglet',sans-serif;font-size:38px;color:var(--pink);line-height:1}
.brand .dot{display:inline-block;width:10px;height:10px;border-radius:50%;background:var(--pink);margin-left:4px;vertical-align:middle}
.main-nav{left:245px;top:91px;width:364px;height:29px;background:linear-gradient(#c8c8c8,#b4b4b4);border-left:2px solid #9c9c9c;border-right:2px solid #9c9c9c;display:flex;justify-content:space-around;align-items:center;padding:0 10px}
.main-nav a{font-family:'Arimo',sans-serif;font-weight:700;font-size:11px;color:#777;text-decoration:none;letter-spacing:.5px}
.main-nav a.current{color:#4a4a4a}

/* slider */
.slider-frame{left:113px;top:162px;width:614px;height:226px;background:linear-gradient(#c9c9c9,#b3b3b3);border-radius:6px;box-shadow:0 6px 14px rgba(0,0,0,.18)}
.slider-stage{left:124px;top:171px;width:593px;height:210px;background:linear-gradient(135deg,#fafafa,#e1e1e1);border:2px solid #9a9a9a}
.slider-art{left:296px;top:0;width:295px;height:206px;background:radial-gradient(ellipse at 70% 80%,#f4f4f4,#d8d8d8 60%,#e8e8e8)}
.hero-line1{left:21px;top:40px;font-size:30px;color:#777}
.hero-line2{left:26px;top:76px;font-size:37px;color:var(--pink)}
.hero-line3{left:26px;top:124px;font-size:22px;color:#6e6e6e}
.hero-copy{left:26px;top:151px;font-size:12.5px;line-height:15px;color:var(--ink-faint);width:270px}
.slide-arrow{top:252px;width:36px;height:46px;background:linear-gradient(#f0429b,var(--pink-dark));border-radius:4px;display:flex;align-items:center;justify-content:center}
.slide-arrow.prev{left:92px}
.slide-arrow.next{left:711px}

/* content panel */
.content-panel{left:102px;top:449px;width:636px;height:336px;background:linear-gradient(#d9d9d9,#cbcbcb);border-radius:6px}
.panel-divider{left:444px;top:449px;width:1px;height:336px;background:#b8b8b8}
.signup-tab{left:126px;top:428px;width:237px;height:45px;background:linear-gradient(#c4c4c4,#adadad);border-radius:6px;box-shadow:0 4px 8px rgba(0,0,0,.15);display:flex;align-items:center;padding-left:13px;font-size:22px;color:#707070;gap:8px}
.signup-tab .go{width:19px;height:19px;border-radius:50%;background:#8c8c8c;display:flex;align-items:center;justify-content:center}
.field{background:var(--field);border:1px solid var(--field-line);border-radius:4px;font-size:10px;color:#7d7d7d;padding-left:11px;display:flex;align-items:center}
.btn-go{left:356px;top:506px;width:35px;height:22px;background:var(--pink);border-radius:4px;color:var(--white);font-family:'Arimo',sans-serif;font-size:12px;display:flex;align-items:center;justify-content:center}
.posts-heading{left:160px;top:548px;font-size:21px;color:#5a5a5a}
.posts-rule{left:129px;top:584px;width:283px;height:1px;background:#a8a8a8}
.post-icon{width:46px;height:46px;border-radius:5px;background:#a9a9a9;display:flex;align-items:center;justify-content:center}
.post-text{left:189px;width:230px;font-family:'Arimo',sans-serif;font-size:7.2px;line-height:9.4px;color:#666}
.post-text strong{display:block;font-size:8.4px;color:#4a4a4a;margin-bottom:2px}

.social{top:427px;width:48px;height:48px;border-radius:50%;background:radial-gradient(circle at 50% 35%,#f4f4f4,#c6c6c6);box-shadow:0 2px 5px rgba(0,0,0,.2);display:flex;align-items:center;justify-content:center;font-family:'Arimo',sans-serif;font-weight:700;font-size:9px;color:#555}
.panel-brand{left:444px;width:294px;top:516px;text-align:center;font-size:38px;color:var(--pink);font-family:'Sniglet',sans-serif}
.video-label{left:444px;width:310px;top:755px;text-align:center;font-size:13px;color:#444}

/* contact section */
.contact-band{left:0;top:796px;width:840px;height:314px;background:linear-gradient(#d8d8d8,#c9c9c9);border-top:2px solid #bcbcbc}
.talk-heading{left:101px;top:813px;font-size:20px;color:#555}
.talk-intro{left:102px;top:846px;width:400px;font-size:12px;line-height:15px;color:#444}
.form-label{left:103px;font-size:12px;color:#444}
.pill{left:200px;width:299px;height:23px;border-radius:12px;background:#c2c2c2;border:1px solid #b0b0b0;box-shadow:inset 0 1px 3px rgba(0,0,0,.12);font-family:'Arimo',sans-serif;font-size:8px;color:#7a7a7a;padding-left:14px;display:flex;align-items:center}
.message{left:200px;top:958px;width:299px;height:89px;border-radius:10px;background:#c2c2c2;border:1px solid #b0b0b0;box-shadow:inset 0 1px 3px rgba(0,0,0,.12);font-family:'Arimo',sans-serif;font-size:8px;color:#7a7a7a;padding:8px 14px}
.btn-submit{left:198px;top:1056px;width:94px;height:36px;border-radius:18px;background:linear-gradient(#f251a3,var(--pink));border:3px solid #bdbdbd;color:var(--white);font-family:'Arimo',sans-serif;font-weight:700;font-size:14px;display:flex;align-items:center;justify-content:center}
.section-divider{left:522px;top:819px;width:1px;height:273px;background:#a8a8a8}
.readmore-heading{left:543px;top:813px;font-size:18px;color:#555}
.readmore-list{left:543px;top:842px;width:196px;list-style:none;font-family:'Arimo',sans-serif;font-size:9px;color:#555}
.readmore-list li{height:21px;display:flex;align-items:center;gap:6px;border-bottom:1px dashed #9a9a9a;margin-left:0}
.readmore-list li::before{content:"\2665";color:var(--pink);font-size:8px}
.contact-row{left:545px;display:flex;font-size:12px;color:#555}
.contact-row .label{width:67px;display:flex;align-items:center;gap:6px}
.contact-row .value{font-family:'Arimo',sans-serif;font-size:9px;line-height:12px;color:#444;padding-top:2px}
.contact-row a{color:#333}

/* footer */
.site-footer{left:0;top:1110px;width:840px;height:90px;background:linear-gradient(#9a9a9a,#8a8a8a);border-top:2px solid #7c7c7c}
.share-bar{left:0;width:840px;top:1137px;display:flex;justify-content:center;gap:4px}
.share-bar span{height:11px;font-family:'Arimo',sans-serif;font-size:6.5px;color:#345;background:#eef1f6;border:1px solid #b9c2d3;border-radius:2px;padding:0 4px;display:flex;align-items:center}
.share-bar span.plus{background:#4b7fc8;color:#fff;border-color:#3a6aab}
.footer-links{left:0;width:840px;top:1157px;text-align:center;font-family:'Arimo',sans-serif;font-size:7px;line-height:9px;color:#f2f2f2}
</style>
</head>
<body>

<header class="abs site-header"></header>
<div class="abs brand">zMatchy<span class="dot"></span></div>
<nav class="abs main-nav">
  <a href="#">WHY</a><a href="#" class="current">HOW IT WORKS</a><a href="#">SIGN UP</a><a href="#">OUR BLOG</a>
</nav>

<section class="hero">
  <div class="abs slider-frame"></div>
  <div class="abs slider-stage">
    <div class="abs slider-art" role="img" aria-label="Silver computer mouse whose cable loops into a heart shape"></div>
    <div class="abs display hero-line1">Connections that</div>
    <div class="abs display hero-line2">just click</div>
    <div class="abs display hero-line3">Love is not discovered ,</div>
    <p class="abs hero-copy">through endless profile questions hair or eye colour, common interests or physical physique.</p>
  </div>
  <div class="abs slide-arrow prev"><svg width="12" height="16" viewBox="0 0 12 16"><path d="M9 2L3 8l6 6" stroke="#fff" stroke-width="3" fill="none"/></svg></div>
  <div class="abs slide-arrow next"><svg width="12" height="16" viewBox="0 0 12 16"><path d="M3 2l6 6-6 6" stroke="#fff" stroke-width="3" fill="none"/></svg></div>
</section>

<section class="member-area">
  <div class="abs content-panel"></div>
  <div class="abs panel-divider"></div>

  <div class="abs display signup-tab">Signup for zMatchy <span class="go"><svg width="8" height="10" viewBox="0 0 8 10"><path d="M2 1l4 4-4 4" stroke="#e5e5e5" stroke-width="2" fill="none"/></svg></span></div>
  <div class="abs field" style="left:128px;top:506px;width:106px;height:22px">User name</div>
  <div class="abs field" style="left:241px;top:506px;width:107px;height:22px">Password</div>
  <div class="abs btn-go">Go</div>

  <svg class="abs" style="left:129px;top:548px" width="28" height="28" viewBox="0 0 28 28">
    <circle cx="14" cy="14" r="14" fill="#777"/>
    <circle cx="9" cy="19" r="2.3" fill="#ddd"/>
    <path d="M7 12a9 9 0 0 1 9 9M7 7a14 14 0 0 1 14 14" stroke="#ddd" stroke-width="2.6" fill="none"/>
  </svg>
  <h2 class="abs display posts-heading" style="font-weight:400">Recent Posts</h2>
  <div class="abs posts-rule"></div>

  <div class="abs post-icon" style="left:129px;top:596px"><svg width="28" height="28" viewBox="0 0 28 28" fill="none" stroke="#e6e6e6" stroke-width="2.5"><path d="M17 4H8v20h14V9z"/><path d="M15 11v10M10 16h10"/></svg></div>
  <div class="abs post-text" style="top:600px"><strong>Lorem ipsum dolor sit amet, consectetur adipiscing elit.</strong>Lorem ipsum dolor sit amet, consectetur adipiscing elit. Donec et ligula at ligula convallis tempus ut non nisl. Integer neque lacus, auctor vel egestas ac, viverra ac nibh.</div>

  <div class="abs post-icon" style="left:129px;top:659px"><svg width="28" height="28" viewBox="0 0 28 28"><rect x="3" y="3" width="22" height="22" rx="5" fill="#bdbdbd"/><circle cx="18" cy="9" r="3" fill="#fff"/><circle cx="10" cy="14" r="3" fill="#fff"/><circle cx="18" cy="19" r="3" fill="#fff"/><path d="M18 9l-8 5 8 5" stroke="#fff" stroke-width="1.6" fill="none"/></svg></div>
  <div class="abs post-text" style="top:663px"><strong>Lorem ipsum dolor sit amet, consectetur adipiscing elit.</strong>Lorem ipsum dolor sit amet, consectetur adipiscing elit. Donec et ligula at ligula convallis tempus ut non nisl. Integer neque lacus, auctor vel egestas ac, viverra ac nibh.</div>

  <div class="abs post-icon" style="left:129px;top:722px"><svg width="28" height="28" viewBox="0 0 28 28"><path d="M14 24C4 17 3 12 3 9.5A5.5 5.5 0 0 1 14 7a5.5 5.5 0 0 1 11 2.5C25 12 24 17 14 24z" fill="#e6e6e6"/></svg></div>
  <div class="abs post-text" style="top:725px"><strong>Lorem ipsum dolor sit amet, consectetur adipiscing elit.</strong>Lorem ipsum dolor sit amet, consectetur adipiscing elit. Donec et ligula at ligula convallis tempus ut non nisl. Integer neque lacus, auctor vel egestas ac, viverra ac nibh.</div>

  <div class="abs social" style="left:470px">Share</div>
  <div class="abs social" style="left:535px">Post</div>
  <div class="abs social" style="left:601px">Link</div>
  <div class="abs social" style="left:666px">Save</div>

  <div class="abs panel-brand">zMatchy</div>

  <svg class="abs" style="left:536px;top:602px" width="124" height="124" viewBox="0 0 124 124">
    <defs>
      <linearGradient id="ringShade" x1="0" y1="0" x2="0" y2="1"><stop offset="0" stop-color="#9a9a9a"/><stop offset="1" stop-color="#6a6a6a"/></linearGradient>
      <radialGradient id="faceShade" cx=".5" cy=".4" r=".6"><stop offset="0" stop-color="#e6e6e6"/><stop offset="1" stop-color="#c2c2c2"/></radialGradient>
    </defs>
    <circle cx="62" cy="62" r="62" fill="url(#ringShade)"/>
    <circle cx="62" cy="62" r="48" fill="url(#faceShade)"/>
    <path d="M50 40v44l35-22z" fill="#7a7a7a"/>
  </svg>
  <div class="abs video-label">Watch a Video</div>
</section>

<section class="contact">
  <div class="abs contact-band"></div>
  <h2 class="abs display talk-heading" style="font-weight:400">Lates Talk to Us:</h2>
  <p class="abs talk-intro">If you have any questions or you want to meet with us, you can contact us with following methods:</p>

  <div class="abs form-label" style="top:897px">Name</div>
  <div class="abs pill" style="top:892px">enter your text here...</div>
  <div class="abs form-label" style="top:928px">Email</div>
  <div class="abs pill" style="top:925px">enter your text here...</div>
  <div class="abs form-label" style="top:956px">Massage</div>
  <div class="abs message">enter your message here...</div>
  <div class="abs btn-submit">Submit</div>

  <div class="abs section-divider"></div>
  <h2 class="abs display readmore-heading" style="font-weight:400">Read More</h2>
  <ul class="abs readmore-list">
    <li>Why zMatchy</li><li>How it works</li><li>Signup</li><li>Login</li><li>About Us</li>
  </ul>

  <div class="abs contact-row" style="top:977px">
    <div class="label"><svg width="18" height="12" viewBox="0 0 18 12"><rect x=".5" y=".5" width="17" height="11" fill="#777"/><path d="M1 1l8 6 8-6" stroke="#ddd" stroke-width="1.2" fill="none"/></svg>Email:</div>
    <div class="value"><a href="#">hello@zmatchy.net</a></div>
  </div>
  <div class="abs contact-row" style="top:1004px">
    <div class="label"><svg width="18" height="14" viewBox="0 0 18 14"><path d="M1 5c0-4 16-4 16 0v2h-4V5H5v2H1z" fill="#777"/><rect x="4" y="7" width="10" height="7" rx="1" fill="#777"/><circle cx="9" cy="10.5" r="2" fill="#ccc"/></svg>Call:</div>
    <div class="value" style="padding-top:6px">+459 80 3172 605<br>Mr. Elan Brevik,<br>Relasationship Manager</div>
  </div>
  <div class="abs contact-row" style="top:1051px">
    <div class="label"><svg width="18" height="13" viewBox="0 0 18 13"><path d="M0 2h6l2 2h10v9H0z" fill="#666"/></svg>Visit:</div>
    <div class="value">14 Orchard Lane, Block - C<br>Lakeview, United States</div>
  </div>
</section>

<footer class="abs site-footer"></footer>
<div class="abs share-bar"><span>Like</span><span>7,231</span><span>Post</span><span>7,231</span><span class="plus">+1</span></div>
<div class="abs footer-links">Home &nbsp;•&nbsp; Why &nbsp;•&nbsp; How It Works &nbsp;•&nbsp; Signup &nbsp;•&nbsp; Our Blog<br>Copyright©2011 zmatchy.net. Privacy Policy &nbsp;|&nbsp; All Rights Reserved.</div>

</body>
</html>
```